Home web page re-vamp

I would like a stylish new home page design for a clients website.
I have included a sitemap to give some guidance.
The site needs to show off the design capabilitiesof the client

```html
<!DOCTYPE html>
<html lang="en">
<head>
<meta charset="utf-8">
<title>Kestrel Architects — Home</title>
<link href="https://fonts.googleapis.com/css2?family=Lato:wght@300;400;700;900&display=swap" rel="stylesheet">
<style>
:root{
  --bg:#35332f;
  --green:#86c232;
  --green-dark:#74ab25;
  --yellow:#e6bd14;
  --yellow-line:#d5ad0c;
  --card:#f7f7f7;
  --ink:#3c3c3c;
  --muted:#5e5e5e;
  --footer:#1b1b1b;
  --footer-text:#c9c9c9;
  --white:#ffffff;
}
*{margin:0;padding:0;box-sizing:border-box}
html,body{width:1200px;height:983px;overflow:hidden}
body{background:var(--bg);font-family:'Lato',sans-serif;position:relative}
.brand{position:absolute;left:96px;top:30px;display:flex;align-items:center;gap:14px}
.brand-mark{width:34px;height:34px;background:var(--yellow)}
.brand-name{font-weight:300;font-size:42px;color:var(--white);letter-spacing:1px}
.contact{position:absolute;left:884px;top:40px;display:flex;align-items:center}
.contact-icon{width:34px;height:40px}
.contact-divider{width:1px;height:42px;background:#55524c;margin:0 15px 0 12px}
.contact-lines{color:#bdbab3;font-size:15px;line-height:25px;letter-spacing:.3px}
.main-nav{position:absolute;left:98px;top:135px;width:254px;height:414px;list-style:none}
.main-nav li{height:59.2px;background:var(--yellow);border-bottom:1px solid var(--yellow-line);display:flex;align-items:center;position:relative}
.main-nav li.active{background:var(--green);border-color:var(--green-dark)}
.main-nav li::after{content:"";position:absolute;left:49px;top:0;bottom:0;width:1px;background:rgba(0,0,0,.06)}
.nav-icon{width:49px;display:flex;justify-content:center}
.nav-icon svg{width:14px;height:14px;fill:var(--white)}
.nav-label{padding-left:16px;color:var(--white);font-size:14px;text-transform:uppercase}
.hero{position:absolute;left:352px;top:135px;width:748px;height:414px;overflow:hidden}
.hero-image{position:absolute;inset:0;background:radial-gradient(ellipse at 55% 60%,#f4f4f4 0%,#d9d9d9 55%,#a9a9a9 100%)}
.hero-title{position:absolute;right:0;top:144px;width:378px;height:63px;background:rgba(134,194,50,.9);color:var(--white);font-weight:900;font-size:27px;display:flex;align-items:center;justify-content:center;letter-spacing:-.3px}
.hero-more{position:absolute;right:0;top:212px;width:125px;height:51px;background:rgba(134,194,50,.9);color:var(--white);font-size:16px;display:flex;align-items:center;justify-content:center}
.hero-arrow{position:absolute;top:278px;width:34px;height:34px;border-radius:50%;background:#2b2b2b;display:flex;align-items:center;justify-content:center}
.hero-arrow svg{width:14px;height:14px;stroke:var(--white);stroke-width:2.5;fill:none}
.features{position:absolute;top:571px;left:0;width:1200px}
.feature{position:absolute;top:0;width:235px;height:282px;background:var(--card);text-align:center}
.feature-icon{position:absolute;left:0;right:0;top:34px;height:60px;display:flex;justify-content:center}
.feature-icon svg{height:60px;width:64px;fill:none;stroke:#4a4a4a;stroke-width:3}
.feature-shadow{position:absolute;left:65px;right:65px;top:112px;height:8px;background:radial-gradient(ellipse at center,rgba(0,0,0,.12),rgba(0,0,0,0) 70%)}
.feature h2{position:absolute;left:0;right:0;top:135px;font-weight:400;font-size:15.5px;color:var(--ink);text-transform:uppercase}
.feature p{position:absolute;left:22px;right:22px;top:164px;font-size:11.8px;line-height:20px;color:var(--muted)}
.feature .btn{position:absolute;left:50%;transform:translateX(-50%);top:219px;width:100px;height:36px;border:1px solid var(--green);border-radius:3px;color:var(--green-dark);font-size:14px;display:flex;align-items:center;justify-content:center}
.site-footer{position:absolute;left:98px;top:874px;width:1002px;height:109px;background:var(--footer)}
.footer-nav{position:absolute;left:30px;top:26px;font-size:13.2px;color:var(--footer-text)}
.footer-nav span{color:#8b8b8b;margin:0 4px}
.copyright{position:absolute;left:30px;top:60px;font-size:12.5px;color:var(--footer-text)}
.social{position:absolute;left:831px;top:42px;display:flex;gap:6px}
.social span{width:23px;height:23px;border:1px solid #6c6c6c;border-radius:50%}
</style>
</head>
<body>

<header>
  <div class="brand"><span class="brand-mark"></span><span class="brand-name">Kestrel Architects</span></div>
  <div class="contact">
    <svg class="contact-icon" viewBox="0 0 24 28"><path fill="#86c232" d="M6 1l4 6-2.5 2.5c1 3.5 3 7 6 9.5L16 17l5 5-3 4C10 25 3 15 2 5z"/></svg>
    <span class="contact-divider"></span>
    <div class="contact-lines">hello@kestrelarchitects.com<br>+44&nbsp; 7000 4821</div>
  </div>
</header>

<ul class="main-nav">
  <li class="active"><span class="nav-icon"><svg viewBox="0 0 16 16"><path d="M8 1l7 6h-2v7H9.5V10h-3v4H3V7H1z"/></svg></span><span class="nav-label">Home</span></li>
  <li><span class="nav-icon"><svg viewBox="0 0 16 16"><circle cx="8" cy="4.5" r="3.5"/><path d="M2 15c0-4 2.5-6 6-6s6 2 6 6z"/></svg></span><span class="nav-label">About Us</span></li>
  <li><span class="nav-icon"><svg viewBox="0 0 16 16"><circle cx="6" cy="9" r="4.5"/><circle cx="12.5" cy="4" r="3"/></svg></span><span class="nav-label">Services</span></li>
  <li><span class="nav-icon"><svg viewBox="0 0 16 16"><path d="M1 2h14v12H1zm2 2v8h10V4zm1 7l3-4 2 2 1.5-1.5L12 11z"/></svg></span><span class="nav-label">Gallery</span></li>
  <li><span class="nav-icon"><svg viewBox="0 0 16 16"><path d="M15 1L1 7l5 2 2 6z"/></svg></span><span class="nav-label">Health &amp; Safety</span></li>
  <li><span class="nav-icon"><svg viewBox="0 0 16 16"><path d="M1 3h14v12H1zm2 4v6h10V7zM4 1h2v3H4zm6 0h2v3h-2z"/></svg></span><span class="nav-label">Specification Sheets</span></li>
  <li><span class="nav-icon"><svg viewBox="0 0 16 16"><path d="M1 6c0-3 14-3 14 0v2h-4V6H5v2H1zm2 3h10v5H3z"/></svg></span><span class="nav-label">Contact Us</span></li>
</ul>

<section class="hero">
  <div class="hero-image" role="img" aria-label="Photo of a white architectural building model under a green crane, resting on rolled blueprints"></div>
  <div class="hero-title">ARCHITECTS &amp; DESIGNERS</div>
  <div class="hero-more">READ MORE</div>
  <div class="hero-arrow" style="left:658px"><svg viewBox="0 0 14 14"><path d="M9 2L4 7l5 5"/></svg></div>
  <div class="hero-arrow" style="left:701px"><svg viewBox="0 0 14 14"><path d="M5 2l5 5-5 5"/></svg></div>
</section>

<section class="features">
  <article class="feature" style="left:98px">
    <div class="feature-icon"><svg viewBox="0 0 64 60"><rect x="4" y="10" width="44" height="44" rx="6"/><path d="M22 40l4-10L52 4l8 8-26 26z" fill="#4a4a4a"/></svg></div>
    <div class="feature-shadow"></div>
    <h2>Why Us</h2>
    <p>7 Days from quotation to delivery using the latest technology</p>
    <span class="btn">READ MORE</span>
  </article>
  <article class="feature" style="left:352px">
    <div class="feature-icon"><svg viewBox="0 0 64 60"><path d="M6 58V22h18v36M24 58V6h22v52M46 58V28h12v30M2 58h60" fill="none"/><path d="M30 14h10M30 22h10M30 30h10M30 38h10M10 30h10M10 38h10" stroke-width="2"/></svg></div>
    <div class="feature-shadow"></div>
    <h2>Architects &amp; Designers</h2>
    <p>Advice on colours and materials Environmental friendly manufacture</p>
    <span class="btn">READ MORE</span>
  </article>
  <article class="feature" style="left:609px">
    <div class="feature-icon"><svg viewBox="0 0 64 60" stroke-width="1.6"><path d="M8 12l24-8 24 8-24 8zM8 12v34l24 10 24-10V12M32 20v36"/><path d="M8 46l24-8 24 8" /><text x="19" y="40" font-family="Lato,sans-serif" font-size="20" font-weight="700" fill="#4a4a4a" stroke="none">3D</text></svg></div>
    <div class="feature-shadow"></div>
    <h2>Commercial Fit</h2>
    <p>Site Surveys and Consultation by our experienced design team</p>
    <span class="btn">READ MORE</span>
  </article>
  <article class="feature" style="left:866px">
    <div class="feature-icon"><svg viewBox="0 0 64 60"><path d="M22 6h20v14c0 8-10 12-10 12S22 28 22 20z" fill="#4a4a4a"/><path d="M10 14c-4 16 4 30 22 36M54 14c4 16-4 30-22 36" stroke-width="4"/></svg></div>
    <div class="feature-shadow"></div>
    <h2>Awards &amp; Accreditations</h2>
    <p>7 Days from quotation to delivery using the latest technology</p>
    <span class="btn">READ MORE</span>
  </article>
</section>

<footer class="site-footer">
  <nav class="footer-nav">Home<span>/</span>About Us<span>/</span>Services<span>/</span>Our Clients<span>/</span>Gallery<span>/</span>Health &amp; Safety<span>/</span>Contact Us</nav>
  <p class="copyright">©2013 - 2014&nbsp; Kestrel Architects , All Rights Reserved.</p>
  <div class="social" aria-label="Social links"><span></span><span></span><span></span><span></span><span></span></div>
</footer>

</body>
</html>
```